CRPG is needing business cards, and stationary created.

Pixel Forge created a logo for our business, and now we are wanting business cards, and stationary. I have included two designs of the same logo. Please feel free to use them as you want. The name of the company is Cedar Ridge Property Group LLC, the address is 812 NE Tamber Ln., Suite 9, the city & state is Bend, Oregon, zip code is 97815, Telephone number is 541-237-4190, Fax number is 541-237-8856, the name on the business card is Travis Lundqor CMCA

Industry/Entity Type

Property Management

Contact Information for Business Card

The card needs to look professional. Upscale.

Requirements
Must have
• The colors we are using are on the logo that has been uploaded.

```html
<!DOCTYPE html>
<html lang="en">
<head>
<meta charset="utf-8">
<title>Cedar Ridge Property Group – Business Card</title>
<link href="https://fonts.googleapis.com/css2?family=Roboto:wght@300;400;500;700&display=swap" rel="stylesheet">
<style>
  :root {
    --teal: #1a8c7a;
    --teal-dark: #177d6d;
    --ink: #5f6368;
    --ink-strong: #4a4d52;
    --paper: #ffffff;
    --paper-tint: #fbfbfb;
    --backdrop: #ffffff;
    --icon-phone: #f06c92;
    --icon-fax: #3bbcc4;
    --icon-pin: #f5961e;
    --light-text: #e9eeed;
  }
  * { box-sizing: border-box; margin: 0; padding: 0; }
  html, body {
    width: 1200px;
    height: 1200px;
    overflow: hidden;
    background: var(--backdrop);
    font-family: "Roboto", Arial, sans-serif;
  }
  .canvas {
    position: relative;
    width: 1200px;
    height: 1200px;
  }
  .card {
    position: absolute;
    left: 222px;
    width: 769px;
    height: 440px;
  }
  .card--front {
    top: 130px;
    background: var(--paper-tint);
    border: 1px solid #f0f0f0;
  }
  .card--back {
    top: 619px;
    background: var(--teal);
  }

  /* Front: brand lockup */
  .brand {
    position: absolute;
    display: flex;
    align-items: center;
    gap: 12px;
  }
  .brand__mark {
    flex: none;
    background: var(--teal);
  }
  .brand__name {
    font-weight: 500;
    text-transform: uppercase;
    line-height: 1.1;
  }
  .card--front .brand {
    left: 42px;
    top: 62px;
  }
  .card--front .brand__mark {
    width: 34px;
    height: 34px;
  }
  .card--front .brand__name {
    color: var(--teal);
    font-size: 21px;
    letter-spacing: 1px;
  }

  /* Front: person */
  .person {
    position: absolute;
    right: 36px;
    top: 100px;
    text-align: right;
  }
  .person__name {
    font-size: 32px;
    font-weight: 300;
    color: var(--ink);
    letter-spacing: -0.5px;
    text-transform: uppercase;
  }
  .person__credential {
    font-weight: 500;
    color: var(--ink-strong);
  }
  .person__rule {
    width: 172px;
    height: 3px;
    background: var(--teal);
    margin: 6px 0 0 auto;
  }

  /* Front: contact list */
  .contact {
    position: absolute;
    left: 44px;
    top: 252px;
    list-style: none;
  }
  .contact__item {
    display: flex;
    align-items: flex-start;
    height: 36px;
  }
  .contact__icon {
    flex: none;
    width: 36px;
    height: 36px;
    display: flex;
    align-items: center;
    justify-content: center;
  }
  .contact__icon--phone { background: var(--icon-phone); }
  .contact__icon--fax { background: var(--icon-fax); }
  .contact__icon--pin { background: var(--icon-pin); }
  .contact__text {
    margin-left: 17px;
    font-size: 20px;
    color: var(--ink);
    line-height: 36px;
  }
  .contact__item--address .contact__text {
    line-height: 26px;
    padding-top: 4px;
  }

  /* Back: centered lockup */
  .card--back .brand {
    left: 0;
    right: 0;
    top: 0;
    bottom: 0;
    flex-direction: column;
    justify-content: center;
    gap: 26px;
  }
  .card--back .brand__mark {
    width: 70px;
    height: 70px;
    background: var(--light-text);
  }
  .card--back .brand__name {
    color: var(--light-text);
    font-size: 50px;
    letter-spacing: 3px;
    text-align: center;
  }
</style>
</head>
<body>
<main class="canvas">

  <section class="card card--front" aria-label="Business card front">
    <div class="brand">
      <span class="brand__mark"></span>
      <span class="brand__name">Cedar Ridge<br>Property Group</span>
    </div>

    <div class="person">
      <h1 class="person__name">Travis Lundqor <span class="person__credential">CMCA</span></h1>
      <div class="person__rule"></div>
    </div>

    <ul class="contact">
      <li class="contact__item">
        <span class="contact__icon contact__icon--phone">
          <svg width="16" height="16" viewBox="0 0 24 24" aria-hidden="true">
            <path fill="#fff" d="M6.6 10.8a15.1 15.1 0 0 0 6.6 6.6l2.2-2.2c.3-.3.7-.4 1-.2 1.1.4 2.3.6 3.6.6.6 0 1 .4 1 1V20c0 .6-.4 1-1 1A17 17 0 0 1 3 4c0-.6.4-1 1-1h3.5c.6 0 1 .4 1 1 0 1.3.2 2.5.6 3.6.1.3 0 .7-.2 1z"/>
          </svg>
        </span>
        <span class="contact__text">541-237-4190</span>
      </li>
      <li class="contact__item">
        <span class="contact__icon contact__icon--fax">
          <svg width="18" height="18" viewBox="0 0 24 24" aria-hidden="true">
            <g fill="none" stroke="#fff" stroke-width="1.6">
              <rect x="3" y="8" width="5" height="13" rx="1"/>
              <rect x="8" y="10" width="13" height="11" rx="1"/>
              <path d="M11 10V3h7v7"/>
              <path d="M12 14h2M16 14h2M12 17h2M16 17h2"/>
            </g>
          </svg>
        </span>
        <span class="contact__text">541-237-8856</span>
      </li>
      <li class="contact__item contact__item--address">
        <span class="contact__icon contact__icon--pin">
          <svg width="14" height="18" viewBox="0 0 14 18" aria-hidden="true">
            <path fill="#fff" d="M7 0a7 7 0 0 0-7 7c0 5 7 11 7 11s7-6 7-11a7 7 0 0 0-7-7zm0 9.5A2.5 2.5 0 1 1 7 4.5a2.5 2.5 0 0 1 0 5z"/>
          </svg>
        </span>
        <span class="contact__text">812 NE Tamber Ln., Suite 9, Bend,<br>Oregon (97815)</span>
      </li>
    </ul>
  </section>

  <section class="card card--back" aria-label="Business card back">
    <div class="brand">
      <span class="brand__mark"></span>
      <span class="brand__name">Cedar Ridge<br>Property Group</span>
    </div>
  </section>

</main>
</body>
</html>
```